Back Pain

Need a flyer similar to the attached draft. This is to be handed out to prospective patients. Note that Artwell Studio has already designed the logo. If you need a copy please contact me

```html
<!DOCTYPE html>
<html lang="en">
<head>
<meta charset="utf-8">
<title>Spinewell Relief Clinic – Tech Neck Flyer</title>
<link rel="stylesheet" href="https://fonts.googleapis.com/css2?family=Barlow+Semi+Condensed:wght@500;600;700&family=Montserrat:ital,wght@0,500;0,600;0,700;1,300&display=swap">
<style>
  :root {
    --ink: #0a0a0a;
    --paper: #ffffff;
    --brand-blue: #1f7fbf;
    --brand-green: #8cc63f;
    --plum: #4a0a45;
    --navy: #0b2f4a;
    --band: #063a5c;
    --magenta: #8a0a8a;
    --lilac: #b57fc0;
    --label-1: #0b4a6a;
    --label-2: #0d5a78;
    --label-3: #0e6a87;
    --label-4: #0e7b96;
    --label-5: #0aa0b8;
    --label-6: #0bbccf;
    --bar-0: #cddbcd;
    --bar-15: #bcd5a0;
    --bar-30: #9cc06a;
    --bar-45: #78a83a;
    --bar-60: #4f8c10;
    --head: #0b2f5a;
    --pie-light: #c08ee6;
    --pie-dark: #8020d0;
  }
  * { margin: 0; padding: 0; box-sizing: border-box; }
  html, body { width: 848px; height: 1200px; overflow: hidden; background: var(--paper); }
  .flyer { position: relative; width: 848px; height: 1200px; overflow: hidden; background: var(--paper); font-family: "Barlow Semi Condensed", sans-serif; color: var(--ink); }
  .abs { position: absolute; }

  .masthead { left: 0; top: 0; width: 848px; height: 158px; background: var(--ink); }
  .brand-dot { left: 172px; top: 28px; width: 100px; height: 100px; border-radius: 50%; background: var(--brand-blue); }
  .brand-name { left: 296px; top: 56px; font-family: "Montserrat", sans-serif; font-weight: 600; font-size: 29px; color: var(--brand-blue); white-space: nowrap; }
  .brand-tagline { left: 298px; top: 91px; font-family: "Montserrat", sans-serif; font-weight: 500; font-size: 14px; letter-spacing: 3.6px; color: var(--brand-blue); white-space: nowrap; }

  .clinic-title { left: 0; width: 848px; top: 180px; text-align: center; padding-left: 28px; font-family: "Montserrat", sans-serif; font-weight: 500; font-size: 40px; letter-spacing: 7px; white-space: nowrap; }
  .headline { left: 0; width: 848px; top: 228px; text-align: center; font-weight: 600; font-size: 88px; line-height: 1; color: var(--plum); letter-spacing: 1px; }

  .figure-area { left: 48px; top: 346px; width: 218px; height: 630px; border-radius: 100px 100px 30px 30px; background: linear-gradient(180deg, #1c1c1c, #000); }

  .symptom { height: 35px; border-radius: 0 6px 6px 0; color: var(--paper); font-weight: 600; font-size: 20px; line-height: 35px; padding-left: 14px; white-space: nowrap; }
  .s1 { left: 206px; top: 365px; width: 136px; background: var(--label-1); padding-left: 20px; }
  .s2 { left: 182px; top: 412px; width: 139px; background: var(--label-2); padding-left: 30px; }
  .s3 { left: 186px; top: 457px; width: 159px; background: var(--label-3); padding-left: 11px; }
  .s4 { left: 186px; top: 502px; width: 116px; background: var(--label-4); padding-left: 15px; }
  .s5 { left: 190px; top: 582px; width: 165px; background: var(--label-5); padding-left: 5px; }
  .s6 { left: 192px; top: 627px; width: 107px; background: var(--label-6); padding-left: 15px; }

  .chart-intro { left: 448px; top: 336px; font-weight: 600; font-size: 21px; line-height: 27px; white-space: nowrap; }
  .chart { left: 440px; top: 360px; }
  .bar-value { font-family: "Barlow Semi Condensed", sans-serif; font-weight: 600; font-size: 27px; fill: var(--paper); text-anchor: middle; }
  .deg { font-family: "Barlow Semi Condensed", sans-serif; font-weight: 600; font-size: 29px; fill: var(--ink); text-anchor: middle; }
  .axis-label { left: 470px; top: 625px; font-weight: 600; font-size: 18px; white-space: nowrap; }
  .y-label { left: 752px; top: 575px; transform: rotate(-90deg); transform-origin: 0 0; font-weight: 600; font-size: 18px; white-space: nowrap; }

  .pie { left: 402px; top: 660px; }
  .stat { left: 520px; top: 680px; font-weight: 600; white-space: nowrap; }
  .stat-small { font-size: 18px; line-height: 21px; letter-spacing: 0.4px; }
  .stat-big { font-size: 30px; line-height: 27px; color: var(--label-1); }

  .pitch { left: 279px; top: 788px; width: 526px; font-weight: 600; text-transform: uppercase; white-space: nowrap; }
  .pitch-line { display: block; line-height: 1; }
  .pl1, .pl3, .pl4 { font-size: 38px; margin-bottom: 5px; }
  .pl2 { font-size: 29px; margin-bottom: 7px; letter-spacing: 0.3px; }
  .dark { color: var(--magenta); }
  .light { color: var(--lilac); }

  .doctor { left: 0; width: 848px; top: 978px; text-align: center; font-family: "Montserrat", sans-serif; font-weight: 600; font-size: 42px; letter-spacing: 2px; color: var(--navy); }
  .location { left: 0; width: 848px; top: 1022px; text-align: center; font-family: "Montserrat", sans-serif; font-weight: 700; font-size: 24px; letter-spacing: 1.6px; color: var(--navy); white-space: nowrap; }

  .offer-band { left: 0; top: 1063px; width: 848px; height: 137px; background: var(--band); font-family: "Montserrat", sans-serif; color: var(--paper); }
  .offer-line1 { position: absolute; left: 38px; top: 12px; white-space: nowrap; }
  .offer-pct { font-weight: 600; font-size: 40px; color: var(--brand-green); letter-spacing: 1px; }
  .offer-text { font-weight: 700; font-size: 26px; letter-spacing: 1.8px; margin-left: 10px; }
  .offer-line2 { position: absolute; left: 38px; top: 60px; white-space: nowrap; }
  .offer-at { font-weight: 700; font-size: 25px; letter-spacing: 1px; }
  .offer-url { font-weight: 700; font-size: 33px; color: var(--brand-green); margin-left: 34px; }
  .offer-note { position: absolute; left: 0; width: 848px; top: 98px; text-align: center; font-weight: 300; font-style: italic; font-size: 33px; }
</style>
</head>
<body>
<main class="flyer">
  <header class="abs masthead">
    <div class="abs brand-dot"></div>
    <div class="abs brand-name">SPINEWELL RELIEF CLINIC</div>
    <div class="abs brand-tagline">DR SAM HARTLEY - CHIROPRACTOR</div>
  </header>

  <h2 class="abs clinic-title">SPINEWELL RELIEF CLINIC</h2>
  <h1 class="abs headline">TECH NECK</h1>

  <div class="abs figure-area" role="img" aria-label="Silhouette of a man walking while looking down at his phone"></div>

  <div class="abs symptom s1">HEADACHES</div>
  <div class="abs symptom s2">NECK PAIN</div>
  <div class="abs symptom s3">SHOULDER PAIN</div>
  <div class="abs symptom s4">BACK PAIN</div>
  <div class="abs symptom s5">ARM &amp; HANDPAIN</div>
  <div class="abs symptom s6">SCIATICA</div>

  <p class="abs chart-intro">AS THE HEAD TILTS FORWARD,<br>MORE FORCE IS PLACED<br>ON THE SPINE</p>

  <svg class="abs chart" width="320" height="260" viewBox="0 0 320 260">
    <rect x="25" y="187" width="44" height="29" fill="var(--bar-0)"/>
    <rect x="81" y="126" width="44" height="90" fill="var(--bar-15)"/>
    <rect x="139" y="80" width="44" height="136" fill="var(--bar-30)"/>
    <rect x="200" y="44" width="44" height="172" fill="var(--bar-45)"/>
    <rect x="257" y="9" width="45" height="207" fill="var(--bar-60)"/>
    <rect x="27" y="72" width="74" height="86" rx="30" fill="var(--head)" role="img" aria-label="Side profile of a head tilted forward"/>
    <text class="bar-value" x="47" y="213">12</text>
    <text class="bar-value" x="103" y="197">27</text>
    <text class="bar-value" x="161" y="178">40</text>
    <text class="bar-value" x="222" y="158">49</text>
    <text class="bar-value" x="280" y="140">60</text>
    <text class="deg" x="44" y="257">0</text><circle cx="58" cy="236" r="3.5" fill="none" stroke="var(--ink)" stroke-width="1"/>
    <text class="deg" x="103" y="257">15</text><circle cx="122" cy="236" r="3.5" fill="none" stroke="var(--ink)" stroke-width="1"/>
    <text class="deg" x="161" y="257">30</text><circle cx="180" cy="236" r="3.5" fill="none" stroke="var(--ink)" stroke-width="1"/>
    <text class="deg" x="221" y="257">45</text><circle cx="240" cy="236" r="3.5" fill="none" stroke="var(--ink)" stroke-width="1"/>
    <text class="deg" x="279" y="257">60</text><circle cx="298" cy="236" r="3.5" fill="none" stroke="var(--ink)" stroke-width="1"/>
  </svg>
  <div class="abs axis-label">DEGREES OF FORWARD HEAD TILT</div>
  <div class="abs y-label">PRESSURE ON SPINE (LBS)</div>

  <svg class="abs pie" width="112" height="112" viewBox="0 0 112 112">
    <circle cx="56" cy="56" r="54" fill="var(--pie-light)"/>
    <path d="M56 56 L59 2 A54 54 0 0 1 88 100 Z" fill="var(--pie-dark)"/>
  </svg>
  <div class="abs stat">
    <div class="stat-small">THE AVERAGE PERSON SPENDS</div>
    <div class="stat-big">8-11 HOURS PER DAY</div>
    <div class="stat-small">USING ELECTRONIC DEVICES</div>
  </div>

  <p class="abs pitch">
    <span class="pitch-line pl1"><span class="dark">Chiropractic care</span> <span class="light">can help</span></span>
    <span class="pitch-line pl2 light">Correct and prevent these problems</span>
    <span class="pitch-line pl3"><span class="light">by</span> <span class="dark">restoring</span> <span class="light">and</span> <span class="dark">maintaning</span></span>
    <span class="pitch-line pl4"><span class="dark">proper alignment</span> <span class="light">of the</span> <span class="dark">neck</span></span>
  </p>

  <div class="abs doctor">DR. SAMUEL HARTLEY</div>
  <div class="abs location">NOW IN HARBOURSIDE AT 42 QUAY RD. STUDIO SUITE</div>

  <footer class="abs offer-band">
    <div class="offer-line1"><span class="offer-pct">50% OFF</span><span class="offer-text">INITIAL CONSULTATION IF YOU BOOK</span></div>
    <div class="offer-line2"><span class="offer-at">ONLINE AT</span><span class="offer-url">www.spinewellclinic.example.au</span></div>
    <div class="offer-note">choose “TECH NECK” option</div>
  </footer>
</main>
</body>
</html>
```